Real Estate Business Folders, Business Cards, Envelopes & Letterhead

Im looking for trendy, modern & professional design concepts for my business folder that will be used for real estate documents and property report presentations. I'm also looking for Business card designs, envelopes and letterhead with a similar theme. I have a logo already and I would like the logo colors to be incorporated in the design concepts.

Target Market(s)

Real Estate Investors, Banks, Financial Institutions

Industry/Entity Type

Real Estate

Colors
0455a3
959595
d3d3d3
848484

Requirements
Must have
• Trendy Modern, High Class look. Please include logo and colors and incorporate some silver or metallic.
• Business Address: 4812 Corvelle Blvd ste 210-300
• Dalmoor Springs, NV 89712
• Phone: 702-555-0147
• Fax : 702-555-0183
• Email: info@mesacrestlandgroup.example
• Website: MesaCrestLandGroup.example

```html
<!DOCTYPE html>
<html lang="en">
<head>
<meta charset="utf-8">
<title>Mesa Crest Land Group – Business Card</title>
<link rel="stylesheet" href="https://fonts.googleapis.com/css2?family=Open+Sans:wght@400;600;700&display=swap">
<style>
  :root {
    --stage: #3a9fe0;
    --brand-blue: #0455a3;
    --brand-blue-light: #6cb2ef;
    --silver: #959595;
    --silver-light: #d3d3d3;
    --silver-dark: #848484;
    --paper: #ffffff;
    --ink-grey: #6f6f6f;
  }
  * { box-sizing: border-box; margin: 0; padding: 0; }
  html, body { width: 1200px; height: 856px; overflow: hidden; }
  body {
    background: var(--stage);
    font-family: "Open Sans", Arial, sans-serif;
    display: flex;
    align-items: center;
    justify-content: center;
    gap: 40px;
  }
  .card {
    width: 540px;
    height: 309px;
    border-radius: 26px;
    position: relative;
    overflow: hidden;
    box-shadow: 0 6px 18px rgba(0, 40, 90, 0.25);
  }

  /* Front */
  .card-front {
    background: linear-gradient(160deg, var(--brand-blue-light) 0%, #2f86d6 45%, var(--brand-blue) 100%);
    display: flex;
    align-items: center;
    justify-content: center;
  }
  .brand-name {
    display: flex;
    align-items: center;
    gap: 12px;
    font-weight: 600;
    letter-spacing: 0.04em;
  }
  .card-front .brand-name { color: var(--paper); font-size: 30px; }
  .card-front .brand-mark { background: var(--paper); width: 30px; height: 30px; flex: none; }

  /* Back */
  .card-back {
    background: var(--paper);
    display: flex;
    align-items: center;
    padding: 0 30px 0 34px;
  }
  .card-back .brand-name { color: var(--brand-blue); font-size: 19px; flex: 0 0 210px; }
  .card-back .brand-mark { background: var(--brand-blue); width: 18px; height: 18px; flex: none; }
  .divider {
    width: 1px;
    align-self: stretch;
    margin: 52px 22px 70px;
    background: linear-gradient(var(--silver-light), var(--silver), var(--silver-light));
  }
  .contact { flex: 1; }
  .person-name { color: var(--brand-blue); font-size: 20px; font-weight: 600; line-height: 1.1; }
  .person-role { color: var(--silver-light); font-size: 11px; margin-bottom: 8px; }
  .contact-line {
    display: flex; align-items: center; gap: 6px;
    font-size: 10.5px; color: var(--ink-grey); line-height: 1.65; white-space: nowrap;
  }
  .contact-line.address { color: var(--brand-blue); font-weight: 700; align-items: flex-start; }
  .contact-line svg { width: 10px; height: 10px; flex: none; fill: var(--brand-blue); }
  .contact-line.address svg { margin-top: 4px; }
  .bottom-stripe {
    position: absolute; left: 0; right: 0; bottom: 0; height: 5px;
    background: linear-gradient(90deg, var(--brand-blue) 0 40%, var(--silver-light) 40% 58%, var(--brand-blue) 58% 100%);
  }
</style>
</head>
<body>

  <section class="card card-front" aria-label="Card front">
    <div class="brand-name"><span class="brand-mark"></span>MESA CREST LAND GROUP</div>
  </section>

  <section class="card card-back" aria-label="Card back">
    <div class="brand-name"><span class="brand-mark"></span><span>MESA CREST<br>LAND GROUP</span></div>
    <div class="divider"></div>
    <div class="contact">
      <p class="person-name">Example Name</p>
      <p class="person-role">Designation</p>
      <p class="contact-line address">
        <svg viewBox="0 0 10 10"><path d="M5 0a3.5 3.5 0 0 0-3.5 3.5C1.5 6 5 10 5 10s3.5-4 3.5-6.5A3.5 3.5 0 0 0 5 0zm0 5a1.4 1.4 0 1 1 0-2.8A1.4 1.4 0 0 1 5 5z"/></svg>
        <span>4812 Corvelle Blvd ste 210-300<br>Dalmoor Springs, NV 89712</span>
      </p>
      <p class="contact-line">
        <svg viewBox="0 0 10 10"><path d="M2 0.5l2 2-1 1.2a6 6 0 0 0 3.3 3.3l1.2-1 2 2L8.3 9.5C4.5 9.5.5 5.5.5 1.7z"/></svg>
        <span>702-555-0147</span>
        <svg viewBox="0 0 10 10"><path d="M2 0h5v3H2zM0 3.5h10V8H8v2H2V8H0zm3 3v2.5h4V6.5z"/></svg>
        <span>702-555-0183</span>
      </p>
      <p class="contact-line">
        <svg viewBox="0 0 10 10"><path d="M0 1.5h10v7H0zm1 1v.3L5 5.5l4-2.7v-.3z"/></svg>
        <span>info@mesacrestlandgroup.example</span>
      </p>
      <p class="contact-line">
        <svg viewBox="0 0 10 10"><circle cx="5" cy="5" r="4.2" fill="none" stroke="#0455a3" stroke-width="1"/><path d="M0.8 5h8.4M5 0.8c-2.2 2.5-2.2 5.9 0 8.4M5 0.8c2.2 2.5 2.2 5.9 0 8.4" fill="none" stroke="#0455a3" stroke-width="0.8"/></svg>
        <span>www.mesacrestlandgroup.example</span>
      </p>
    </div>
    <div class="bottom-stripe"></div>
  </section>

</body>
</html>
```